依頼詳細
先代経営者から譲り受けた店内のダルマをキャラクター(写真あり。写真を元に名刺にイラスト化しそれをキャラクターとして載せたい)にして親しみのある温かみのある名刺兼ショップカードにしたい。
記載項目
串かつ ほたる
〒579-8042大阪府東大阪市柳原東4丁目17-8
06-6123-4987
希望イメージ
シンプル 複雑
単色 カラフル
暗い 明るい
日常 高級
遊び心 厳粛
未来的 伝統的
女性的 男性的
希望する色
赤系
納品ファイル
補足説明
■ 選んだ理由

色使いの良さとだるまの大きさのインパクトそして少し傾けたイラストそれが印象的であまり可愛すぎもなく、電話番号の視認性も良くだるまの写真にほぼ忠実にイラストを化していただきました。だるまの左下に添えた串カツのイラストも当店が何の店か誰にでもすぐわかります。大変気に入っておりますありがとうございます。

■ 提案者全員のお礼・コメント

今回ご提案していただいたランサーの方々お忙しい中デザインしていただき本当にありがとうございました。皆さん素敵なデザインのイラストのご提案でしたが今回は当選には至りませんでしたがまた別の機会でマッチングすることがあるかもしれないです。末筆ながらますますのご発展お祈り申し上げます。

```html
<!DOCTYPE html>
<html lang="ja">
<head>
<meta charset="utf-8">
<title>串かつ ほたる ショップカード</title>
<link rel="stylesheet" href="https://fonts.googleapis.com/css2?family=Noto+Serif+JP:wght@400;700&display=swap">
<style>
  :root {
    --backdrop: #ecebe8;
    --paper: #f7f5f0;
    --paper-edge: #e2ded6;
    --brand-red: #d7161f;
    --ink: #2b2b2b;
    --ink-soft: #555;
  }
  * { margin: 0; padding: 0; box-sizing: border-box; }
  html, body {
    width: 1200px;
    height: 2856px;
    overflow: hidden;
    background: var(--backdrop);
  }
  .shop-card {
    position: absolute;
    left: 50px;
    top: 518px;
    width: 1100px;
    height: 1820px;
    background: var(--paper);
    border: 1px solid var(--paper-edge);
    box-shadow: 0 14px 40px rgba(0,0,0,0.12);
    font-family: "Noto Serif JP", serif;
    color: var(--ink);
    overflow: hidden;
  }
  .shop-name {
    position: absolute;
    top: 150px;
    left: 300px;
    display: flex;
    flex-direction: row-reverse;
    align-items: flex-start;
    gap: 24px;
    color: var(--brand-red);
    font-weight: 700;
  }
  .shop-name__genre {
    writing-mode: vertical-rl;
    font-size: 64px;
    letter-spacing: 8px;
    line-height: 1;
  }
  .shop-name__main {
    writing-mode: vertical-rl;
    font-size: 230px;
    line-height: 1;
    letter-spacing: 10px;
  }
  .mascot {
    position: absolute;
    left: 60px;
    top: 1130px;
    width: 500px;
    height: 580px;
    transform: rotate(-10deg);
  }
  .shop-info {
    position: absolute;
    left: 600px;
    top: 1470px;
    width: 460px;
    font-size: 30px;
    line-height: 1.6;
    color: var(--ink-soft);
  }
  .shop-info__tel {
    margin-top: 10px;
    font-size: 40px;
    font-weight: 700;
    color: var(--ink);
    letter-spacing: 1px;
  }
</style>
</head>
<body>
  <main class="shop-card">
    <h1 class="shop-name">
      <span class="shop-name__genre">串かつ</span>
      <span class="shop-name__main">ほたる</span>
    </h1>

    <svg class="mascot" viewBox="0 0 500 580" role="img" aria-label="店内のだるまをもとにしたキャラクターイラストと串かつのイラスト">
      <defs>
        <radialGradient id="mascotTone" cx="50%" cy="45%" r="60%">
          <stop offset="0%" stop-color="#f3e9e4"/>
          <stop offset="55%" stop-color="#e25a5d"/>
          <stop offset="100%" stop-color="#d7161f"/>
        </radialGradient>
      </defs>
      <ellipse cx="250" cy="300" rx="230" ry="270" fill="url(#mascotTone)"/>
    </svg>

    <address class="shop-info" style="font-style: normal;">
      <p>〒579-8042</p>
      <p>大阪府東大阪市柳原東4丁目17-8</p>
      <p class="shop-info__tel">TEL 06-6123-4987</p>
    </address>
  </main>
</body>
</html>
```